" Empresa focada em seguros pessoais, tais como seguro saúde, vida, previdência e odontológico, oferecendo segurança e agilidade na contrataçao e manutençao e também qualidade de vida. "

```html
<!DOCTYPE html>
<html lang="pt-BR">
<head>
<meta charset="UTF-8">
<title>Assinatura de E-mail — Lumeva</title>
<link rel="stylesheet" href="https://fonts.googleapis.com/css2?family=Roboto:wght@300;400;500&display=swap">
<style>
  :root {
    --page: #e9ebee;
    --card: #ffffff;
    --navy: #1f3f8c;
    --teal: #2bb3c9;
    --teal-light: #4cc3d6;
    --grey-text: #6b6f78;
  }
  * { margin: 0; padding: 0; box-sizing: border-box; }
  html, body {
    width: 1200px; height: 1200px; overflow: hidden;
    background: var(--page);
    font-family: "Roboto", Arial, sans-serif;
  }
  .signature {
    position: absolute;
    left: 67px; top: 449px;
    width: 1066px; height: 264px;
    background: var(--card);
    box-shadow: 0 4px 14px rgba(0,0,0,0.12);
    overflow: hidden;
  }
  .signature__tab {
    position: absolute;
    left: -12px; top: 26px;
    width: 32px; height: 210px;
    background: var(--navy);
    border-radius: 14px;
  }
  .signature__panel {
    position: absolute;
    right: 0; top: 0;
    width: 115px; height: 100%;
    background: var(--teal-light);
  }
  .brand {
    position: absolute;
    left: 168px; top: 100px;
    display: flex; align-items: center; gap: 14px;
  }
  .brand__dot {
    width: 42px; height: 42px; border-radius: 50%;
    background: var(--teal);
  }
  .brand__divider {
    width: 2px; height: 52px; background: var(--navy); opacity: .6;
  }
  .brand__text { display: flex; flex-direction: column; }
  .brand__name {
    font-size: 40px; font-weight: 400; color: var(--navy);
    line-height: 1; letter-spacing: -0.5px;
  }
  .brand__tagline {
    font-size: 11px; font-weight: 400; color: var(--teal);
    margin-top: 4px; letter-spacing: .3px;
  }
  .contact {
    position: absolute;
    right: 264px; top: 66px;
    text-align: right;
    color: var(--grey-text);
  }
  .contact__name {
    font-size: 19px; font-weight: 500; color: var(--navy);
  }
  .contact__role {
    font-size: 13px; font-weight: 300; margin-bottom: 18px;
  }
  .contact__line {
    font-size: 13px; font-weight: 300; line-height: 17px;
  }
</style>
</head>
<body>
  <section class="signature" aria-label="Assinatura de e-mail">
    <div class="signature__tab"></div>
    <div class="signature__panel"></div>

    <div class="brand">
      <span class="brand__dot"></span>
      <span class="brand__divider"></span>
      <div class="brand__text">
        <span class="brand__name">Lumeva</span>
        <span class="brand__tagline">Consultoria de Benefícios</span>
      </div>
    </div>

    <div class="contact">
      <p class="contact__name">Nome Sobrenome</p>
      <p class="contact__role">Cargo</p>
      <p class="contact__line">Av. Lumeva</p>
      <p class="contact__line">(11) 0000-0000</p>
      <p class="contact__line">(11) 0000-0000</p>
      <p class="contact__line">contato@lumeva.com.br</p>
    </div>
  </section>
</body>
</html>
```